Business Card Design

Design new business card using new logo attached and some details as old business card, which is also attached.

Industry/Entity Type

Business

```html
<!DOCTYPE html>
<html lang="en">
<head>
<meta charset="utf-8">
<title>Daniel R. Whitford CPA, PA – Business Cards</title>
<link href="https://fonts.googleapis.com/css2?family=Inter:wght@300;400&display=swap" rel="stylesheet">
<style>
  :root {
    --ink: #000000;
    --paper: #ffffff;
    --ice: #b7d9dd;
    --plum-light: #6d4290;
    --plum-deep: #54156c;
    --mark: #5a1d72;
  }
  * { margin: 0; padding: 0; box-sizing: border-box; }
  html, body {
    width: 976px;
    height: 1200px;
    overflow: hidden;
    background: var(--paper);
  }
  body {
    position: relative;
    font-family: "Inter", "Helvetica Neue", Arial, sans-serif;
    font-weight: 300;
    color: var(--paper);
  }
  .card {
    position: absolute;
    left: 0;
    width: 976px;
    height: 577px;
    overflow: hidden;
    background: var(--ink);
  }
  .card--front { top: 0; }
  .card--back { top: 625px; height: 575px; }
  .card__art {
    position: absolute;
    inset: 0;
    width: 100%;
    height: 100%;
  }
  .card__mark {
    position: absolute;
    left: 48px;
    top: 78px;
    width: 64px;
    height: 64px;
    border-radius: 50%;
    background: var(--mark);
  }
  .card__name {
    position: absolute;
    left: 141px;
    top: 62px;
    font-size: 45px;
    font-weight: 300;
    letter-spacing: -0.3px;
    white-space: nowrap;
  }
  .card__credential {
    font-size: 27px;
    font-weight: 300;
    margin-left: 6px;
  }
  .card__tagline {
    position: absolute;
    left: 141px;
    top: 122px;
    font-size: 29px;
    line-height: 38px;
    color: var(--ice);
    white-space: nowrap;
  }
  .card__address {
    position: absolute;
    left: 50px;
    top: 232px;
    font-size: 27px;
    line-height: 37px;
    font-style: normal;
    white-space: nowrap;
  }
  .card__contacts {
    position: absolute;
    left: 50px;
    top: 339px;
    font-size: 27px;
    line-height: 36.5px;
    border-collapse: collapse;
  }
  .card__contacts th {
    font-weight: 300;
    text-align: left;
    width: 136px;
    padding: 0;
  }
  .card__contacts td { padding: 0; white-space: nowrap; }
  .card__web {
    position: absolute;
    top: 484px;
    font-size: 40px;
    font-weight: 300;
    letter-spacing: 0.2px;
    white-space: nowrap;
  }
  .card--front .card__web { left: 147px; }
  .card--back .card__web { left: 50px; }
</style>
</head>
<body>

<section class="card card--front">
  <svg class="card__art" viewBox="0 0 976 577" preserveAspectRatio="none" aria-hidden="true">
    <defs>
      <linearGradient id="plumFront" x1="0" y1="0" x2="1" y2="0">
        <stop offset="0.68" stop-color="var(--plum-light)"/>
        <stop offset="1" stop-color="var(--plum-deep)"/>
      </linearGradient>
    </defs>
    <rect width="976" height="577" fill="url(#plumFront)"/>
    <path d="M0,0 H700 A420 420 0 0 1 720,577 H0 Z" fill="var(--ice)" stroke="var(--ink)" stroke-width="2"/>
    <path d="M0,0 H650 A400 400 0 0 1 650,577 H0 Z" fill="var(--paper)"/>
    <path d="M0,0 H615 A379 379 0 0 1 615,577 H0 Z" fill="var(--ink)"/>
  </svg>
  <span class="card__mark"></span>
  <h1 class="card__name">Daniel R. Whitford<span class="card__credential">CPA, PA</span></h1>
  <p class="card__tagline">A Florida Professional Association<br>Tax, Accounting &amp; Advisory Services</p>
  <address class="card__address">240 Harbor Pointe Avenue,<br>Seagrove Bay, FL 32459</address>
  <table class="card__contacts">
    <tr><th>Phone:</th><td>(850) 555 0148</td></tr>
    <tr><th>Mobile:</th><td>(256) 555 0193</td></tr>
    <tr><th>E-Mail:</th><td>dan@drwcpapa.com</td></tr>
  </table>
  <p class="card__web">WWW.DRWCPAPA.COM</p>
</section>

<section class="card card--back">
  <svg class="card__art" viewBox="0 0 976 575" preserveAspectRatio="none" aria-hidden="true">
    <defs>
      <linearGradient id="plumBack" x1="0" y1="0" x2="1" y2="0">
        <stop offset="0.68" stop-color="var(--plum-light)"/>
        <stop offset="1" stop-color="var(--plum-deep)"/>
      </linearGradient>
    </defs>
    <rect width="976" height="575" fill="url(#plumBack)"/>
    <path d="M0,0 H700 A420 420 0 0 1 720,575 H0 Z" fill="var(--ice)" stroke="var(--ink)" stroke-width="2"/>
    <path d="M0,0 H650 A400 400 0 0 1 650,575 H0 Z" fill="var(--paper)"/>
    <path d="M0,0 H615 A379 379 0 0 1 615,575 H0 Z" fill="var(--ink)"/>
  </svg>
  <span class="card__mark"></span>
  <h2 class="card__name">Daniel R. Whitford<span class="card__credential">CPA, PA</span></h2>
  <p class="card__tagline">A Florida Professional Association<br>Tax, Accounting &amp; Advisory Services</p>
  <address class="card__address">240 Harbor Pointe Avenue,<br>Seagrove Bay, FL 32459</address>
  <table class="card__contacts">
    <tr><th>Phone:</th><td>(850) 555 0148</td></tr>
    <tr><th>Mobile:</th><td>(256) 555 0193</td></tr>
    <tr><th>E-Mail:</th><td>dan@drwcpapa.com</td></tr>
  </table>
  <p class="card__web">WWW.DRWCPAPA.COM</p>
</section>

</body>
</html>
```